Timid Kitten Clinic Business Card Design

I need a business card designed for my cat only veterinary clinic. I will upload the logo that I would like included on the card. Please include:
Business Name: The Timid Kitten Clinic
Address: 4827 W. 39th Ln, Scottsdale, AZ 85317
Phone #: 480-555-6314
Website URL: www.timidkittenvet.example
And the Doctors Name: Marla Quint, DVM

```html
<!DOCTYPE html>
<html lang="en">
<head>
<meta charset="utf-8">
<title>The Timid Kitten Clinic – Business Card</title>
<link href="https://fonts.googleapis.com/css2?family=Comfortaa:wght@500;600;700&family=Courgette&display=swap" rel="stylesheet">
<style>
  :root {
    --stage: #ababab;
    --card-front: #fcfcfc;
    --card-back: #5282b8;
    --ink-dark: #1e1e24;
    --ink-blue: #5b82b5;
    --ink-magenta: #d63bbd;
    --logo-fill: #3a1f4a;
    --badge-edge: #3fb3a6;
    --white: #ffffff;
    --shadow: rgba(0, 0, 0, 0.35);
  }
  * { margin: 0; padding: 0; box-sizing: border-box; }
  html, body { width: 1200px; height: 1000px; overflow: hidden; background: var(--stage); }
  body { position: relative; font-family: "Comfortaa", sans-serif; }

  .card {
    position: absolute;
    left: 294px;
    width: 613px;
    height: 352px;
    border-radius: 24px;
    box-shadow: 0 18px 40px var(--shadow);
    overflow: hidden;
  }
  .card--front { top: 93px; background: var(--card-front); }
  .card--back { top: 515px; background: var(--card-back); }

  .brand {
    position: absolute;
    top: 28px;
    left: 0; right: 0;
    display: flex;
    justify-content: center;
    align-items: center;
    gap: 10px;
  }
  .brand__mark {
    width: 86px; height: 86px;
    border-radius: 50%;
    background: var(--logo-fill);
    flex: none;
  }
  .brand__name {
    font-weight: 600;
    font-size: 18px;
    line-height: 1.2;
    letter-spacing: 0.5px;
    color: var(--ink-dark);
  }

  .doctor {
    position: absolute;
    top: 146px;
    left: 0; right: 0;
    text-align: center;
    font-family: "Courgette", cursive;
    font-size: 44px;
    color: var(--ink-magenta);
  }

  .contact {
    position: absolute;
    top: 260px;
    left: 0; right: 0;
    text-align: center;
    font-weight: 600;
    color: var(--ink-blue);
  }
  .contact__phone { font-size: 21px; line-height: 32px; }
  .contact__address { font-size: 19px; line-height: 32px; }

  .back__title {
    position: absolute;
    top: 80px;
    left: 0; right: 0;
    text-align: center;
    font-weight: 600;
    font-size: 46px;
    line-height: 54px;
    letter-spacing: 1.5px;
    color: var(--white);
    text-shadow: 0 2px 4px rgba(0, 0, 0, 0.25);
  }
  .back__url {
    position: absolute;
    top: 192px;
    left: 0; right: 0;
    text-align: center;
    font-weight: 600;
    font-size: 23px;
    letter-spacing: 1px;
    color: var(--white);
  }
  .back__badge {
    position: absolute;
    top: 252px;
    left: 240px;
    width: 134px;
    height: 48px;
  }
</style>
</head>
<body>

  <section class="card card--front">
    <div class="brand">
      <div class="brand__mark"></div>
      <div class="brand__name">The Timid Kitten<br>Clinic</div>
    </div>
    <p class="doctor">Dra. Marla Quint</p>
    <div class="contact">
      <p class="contact__phone">(480) 555-6314</p>
      <p class="contact__address">4827 W. 39th Ln, Scottsdale, AZ 85317</p>
    </div>
  </section>

  <section class="card card--back">
    <h1 class="back__title">The Timid<br>Kitten Clinic</h1>
    <p class="back__url">timidkittenvet.example</p>
    <svg class="back__badge" viewBox="0 0 134 48" role="img" aria-label="Practice certification badge">
      <rect x="1.5" y="1.5" width="131" height="45" rx="22" fill="#ffffff" stroke="#3fb3a6" stroke-width="3"/>
    </svg>
  </section>

</body>
</html>
```